standardize print collateral

we need help standardizing all print collateral and website. top priorities:

1. standardized case studies template
2. standardized marketing slicks template
3. standardized powerpoint template
Updates

Project Deadline Extended
Reason: We are extending the project to allow current design submissions to be tweaked while providing the opportunity for new designs to be submitted. We will need all 3 collateral designs submitted to make a final decision. Please note, these 3 designs should all look different, needless to say they should all compliment eachother. As for some direction, the powerpoint main color should not be yellow since yellow does not show up the same shade on any screen. The case study and marketing slicks will be printed and often sit next to our competitors marketing material - think high end product, technology, revolutionary, edgy, professional. The designs should compliment eachother and feel like the Brightfen Metrics brand (which you are determining) and should stand out professionally. We are open to introducing new colors into our brand, the only thing that must remain the same is our logo. Have fun, make it edgy, and keep it professional. Looking forward to seeing what you submit!

Target Market(s)

Property Casualty Insurance Companies: Executive level wording with actuarial credibility

Industry/Entity Type

Marketing

Requirements
Must have
• professional layout for existing collateral and 2-page marketing slicks. style guide/colors can be transferred to powerpoint. logo must stay; everything else (i.e. color, font, layout/structure etc.) is flexible. The three components should not looks the same, they should only compliment eachother.
Nice to have
• we are revolutionizing a conservative industry, so adequate level of edgy/advanced technology/impactful feel to layout
Should not have
• no need to stay within color constraints of yellow, but need to appropriately work well with the eagle head logo

```html
<!DOCTYPE html>
<html lang="en">
<head>
<meta charset="utf-8">
<title>Rapid Portfolio Analysis — Brightfen Metrics</title>
<link href="https://fonts.googleapis.com/css2?family=Barlow:wght@300;400;500;600;700&display=swap" rel="stylesheet">
<style>
  :root {
    --backdrop: #9a9a9a;
    --paper: #ffffff;
    --navy: #0b2a55;
    --ink-dark: #101418;
    --gold: #f0b323;
    --cyan: #16aee8;
    --cyan-deep: #0aa4e0;
    --sand: #f8e7cc;
    --body: #3d3d3d;
    --rule: #c9c9c9;
  }
  * { margin: 0; padding: 0; box-sizing: border-box; }
  html, body { width: 1200px; height: 900px; overflow: hidden; }
  body { background: var(--backdrop); font-family: "Barlow", Arial, sans-serif; position: relative; }

  .sheet { position: absolute; left: 280px; top: 25px; width: 650px; height: 842px; background: var(--paper); overflow: hidden; }

  .hero { position: absolute; left: 0; top: 0; width: 650px; height: 310px; background: var(--ink-dark); }
  .hero-band { position: absolute; left: 0; top: 0; width: 650px; height: 102px;
    background: linear-gradient(90deg, #0a2147 0%, #123c78 60%, #0d2c5c 100%); }
  .hero-title { position: absolute; left: 48px; top: 58px; color: #fff; font-weight: 300; font-size: 30px; letter-spacing: 0.2px; }
  .hero-photo { position: absolute; left: 390px; top: 102px; width: 260px; height: 208px;
    background: radial-gradient(ellipse at 60% 45%, #3b4552 0%, #1a2028 55%, #0e1116 100%); }
  .hero-tag { position: absolute; left: 0; top: 102px; width: 390px; height: 33px; background: var(--gold);
    color: #fff; font-weight: 600; font-size: 17px; line-height: 33px; padding-left: 47px; }
  .hero-intro { position: absolute; left: 47px; top: 152px; width: 322px; color: #fff; font-weight: 600; font-size: 10.3px; line-height: 15.1px; }

  .tab-cyan { position: absolute; left: 0; top: 333px; width: 175px; height: 26px; background: var(--cyan);
    color: #fff; font-weight: 700; font-size: 14px; line-height: 26px; padding-left: 47px; }
  .steps { position: absolute; left: 47px; top: 368px; width: 268px; }
  .step-title { color: var(--cyan); font-weight: 700; font-size: 12.5px; margin-bottom: 3px; }
  .step-text { color: var(--body); font-size: 10.3px; line-height: 12.6px; margin-bottom: 10px; }

  .side { position: absolute; left: 346px; top: 320px; width: 304px; height: 382px; background: var(--sand); }
  .side-title { position: absolute; left: 14px; font-weight: 700; font-size: 12.5px; color: #111; }
  .side-caption { position: absolute; left: 14px; width: 270px; font-size: 8.6px; line-height: 11px; color: #222; }
  .metric-table { position: absolute; left: 14px; top: 35px; width: 245px; height: 120px; border-collapse: collapse; background: #fff; font-size: 4.6px; color: #333; }
  .metric-table th { font-weight: 700; padding: 1px; border-bottom: 0.5px solid var(--rule); }
  .metric-table td { padding: 0 2px; text-align: right; border-bottom: 0.3px solid #e6e6e6; }
  .metric-table .hot { background: #f29b7a; }
  .metric-table .warm { background: #f7d56a; }
  .metric-table .cool { background: #8fcf7c; }
  .dist-chart { position: absolute; left: 14px; top: 222px; }

  .tab-dark { position: absolute; left: 0; top: 712px; width: 438px; height: 26px; background: #000;
    color: var(--gold); font-weight: 700; font-size: 14px; line-height: 26px; padding-left: 47px; z-index: 2; }
  .closing { position: absolute; left: 0; top: 712px; width: 650px; height: 130px; background: var(--cyan-deep); }
  .closing-text { position: absolute; left: 47px; top: 36px; width: 560px; color: #fff; font-weight: 600; font-size: 11px; line-height: 14px; }
</style>
</head>
<body>
<main class="sheet">
  <header class="hero">
    <div class="hero-band"></div>
    <h1 class="hero-title">Rapid Portfolio Analysis</h1>
    <div class="hero-photo" role="img" aria-label="Photo of a businessman touching glowing touchscreen buttons with an outstretched hand"></div>
    <h2 class="hero-tag">Winning Against Adverse Selection</h2>
    <p class="hero-intro">The property and casualty market is over-supplied with excess capacity, and current pricing methods are inconsistent and outdated. This leads to a considerable level of adverse selection within nearly every portfolio. Almost every insurer is attracting customers who are underpriced and losing business where they are overpriced. This invisible effect only surfaces after evidence of slowly deteriorating portfolio loss ratios, resulting in premium increases across the portfolio. These across-the-board premium increases exacerbate the problem by overpricing the most profitable customers and driving them into the arms of competitors.</p>
  </header>

  <h2 class="tab-cyan">How does it work?</h2>
  <section class="steps">
    <h3 class="step-title">Detection: Is the portfolio priced correctly?</h3>
    <p class="step-text">Vantor employs a regression method based on a technological breakthrough. It exposes pricing imbalances by commonly employed rating methods including the GLM. These pricing imbalances are the major drivers of adverse selection.</p>
    <h3 class="step-title">Measurement: How is the portfolio trending?</h3>
    <p class="step-text">Vantor scores the two most important attributes of the portfolio: the adequacy of rates and the quality of the business on a progressive basis. In addition, Vantor projects the financial outcome of business as it is written with startling accuracy. Insurers are able to know significantly in advance of trends in their business.</p>
    <h3 class="step-title">Correction: How to address the issues?</h3>
    <p class="step-text">Vantor provides an array of options for addressing any deterioration in the portfolio. These options range from specifically designed rate adjustments and underwriting strategies, to simple distribution management sales and profitability strategies.</p>
  </section>

  <aside class="side">
    <h3 class="side-title" style="top:15px">Portfolio Monitoring</h3>
    <table class="metric-table">
      <tr><th>Period</th><th>Exposure</th><th>Premium</th><th>Losses</th><th>Ratio</th><th>Rate</th><th>Score</th></tr>
      <tr><td>2001Q1</td><td>35,900</td><td>11,918</td><td>9,540</td><td>79.0%</td><td class="warm">0.968</td><td>523</td></tr>
      <tr><td>2001Q2</td><td>43,828</td><td>14,425</td><td>6,216</td><td>43.1%</td><td class="hot">0.936</td><td>502</td></tr>
      <tr><td>2001Q3</td><td>43,883</td><td>14,027</td><td>9,596</td><td>68.4%</td><td class="warm">0.992</td><td>500</td></tr>
      <tr><td>2001Q4</td><td>37,145</td><td>13,390</td><td>8,257</td><td>61.7%</td><td class="warm">0.97</td><td>524</td></tr>
      <tr><td>2007Q1</td><td>37,988</td><td>21,205</td><td>9,342</td><td>44.0%</td><td class="cool">1.044</td><td>495</td></tr>
      <tr><td>2007Q2</td><td>47,247</td><td>23,940</td><td>7,413</td><td>30.9%</td><td class="cool">1.042</td><td>502</td></tr>
      <tr><td>2007Q3</td><td>40,984</td><td>20,475</td><td>8,208</td><td>40.0%</td><td class="cool">1.033</td><td>501</td></tr>
      <tr><td>2007Q4</td><td>36,924</td><td>22,980</td><td>10,984</td><td>47.7%</td><td class="cool">1.078</td><td>482</td></tr>
      <tr><td>2008Q1</td><td>40,671</td><td>21,959</td><td>7,180</td><td>32.7%</td><td class="cool">1.078</td><td>498</td></tr>
      <tr><td>Total</td><td>1,211,763</td><td>595,065</td><td>292,385</td><td>49.0%</td><td>1</td><td>510</td></tr>
    </table>
    <p class="side-caption" style="top:161px">Predict the future loss ratio of the business being written - both renewals and new business.</p>

    <h3 class="side-title" style="top:202px">Distribution Monitoring</h3>
    <svg class="dist-chart" width="245" height="113" viewBox="0 0 242 112" aria-label="Distribution outlet scorecard chart">
      <rect width="242" height="112" fill="#fff"/>
      <rect x="0" y="0" width="242" height="24" fill="#e4e4e4"/>
      <rect x="6" y="6" width="54" height="12" fill="#3d9a3a"/>
      <rect x="62" y="6" width="56" height="12" fill="#f0c419"/>
      <rect x="124" y="6" width="56" height="12" fill="#d9dde3"/>
      <rect x="184" y="6" width="52" height="12" fill="#7d8fa6"/>
      <rect x="0" y="26" width="242" height="6" fill="#b7dcf2"/>
      <g>
        <rect x="54" y="35" width="30" height="4" fill="#2e8b3a"/><rect x="84" y="35" width="16" height="4" fill="#f0c419"/><rect x="100" y="35" width="12" height="4" fill="#d9362b"/>
        <rect x="54" y="42" width="22" height="4" fill="#2e8b3a"/><rect x="76" y="42" width="24" height="4" fill="#f0c419"/><rect x="100" y="42" width="12" height="4" fill="#d9362b"/>
        <rect x="54" y="49" width="34" height="4" fill="#2e8b3a"/><rect x="88" y="49" width="14" height="4" fill="#f0c419"/><rect x="102" y="49" width="10" height="4" fill="#d9362b"/>
        <rect x="54" y="56" width="26" height="4" fill="#2e8b3a"/><rect x="80" y="56" width="20" height="4" fill="#f0c419"/><rect x="100" y="56" width="12" height="4" fill="#d9362b"/>
        <rect x="54" y="63" width="18" height="4" fill="#2e8b3a"/><rect x="72" y="63" width="26" height="4" fill="#f0c419"/><rect x="98" y="63" width="14" height="4" fill="#d9362b"/>
        <rect x="54" y="70" width="30" height="4" fill="#2e8b3a"/><rect x="84" y="70" width="18" height="4" fill="#f0c419"/><rect x="102" y="70" width="10" height="4" fill="#d9362b"/>
        <rect x="54" y="77" width="24" height="4" fill="#2e8b3a"/><rect x="78" y="77" width="22" height="4" fill="#f0c419"/><rect x="100" y="77" width="12" height="4" fill="#d9362b"/>
        <rect x="54" y="84" width="32" height="4" fill="#2e8b3a"/><rect x="86" y="84" width="16" height="4" fill="#f0c419"/><rect x="102" y="84" width="10" height="4" fill="#d9362b"/>
        <rect x="54" y="91" width="20" height="4" fill="#2e8b3a"/><rect x="74" y="91" width="26" height="4" fill="#f0c419"/><rect x="100" y="91" width="12" height="4" fill="#d9362b"/>
        <rect x="54" y="98" width="28" height="4" fill="#2e8b3a"/><rect x="82" y="98" width="20" height="4" fill="#f0c419"/><rect x="102" y="98" width="10" height="4" fill="#d9362b"/>
      </g>
      <g fill="#bdbdbd">
        <rect x="4" y="36" width="40" height="2"/><rect x="4" y="43" width="40" height="2"/><rect x="4" y="50" width="40" height="2"/><rect x="4" y="57" width="40" height="2"/><rect x="4" y="64" width="40" height="2"/><rect x="4" y="71" width="40" height="2"/><rect x="4" y="78" width="40" height="2"/><rect x="4" y="85" width="40" height="2"/><rect x="4" y="92" width="40" height="2"/><rect x="4" y="99" width="40" height="2"/>
        <rect x="122" y="36" width="70" height="2"/><rect x="122" y="43" width="70" height="2"/><rect x="122" y="50" width="70" height="2"/><rect x="122" y="57" width="70" height="2"/><rect x="122" y="64" width="70" height="2"/><rect x="122" y="71" width="70" height="2"/><rect x="122" y="78" width="70" height="2"/><rect x="122" y="85" width="70" height="2"/><rect x="122" y="92" width="70" height="2"/><rect x="122" y="99" width="70" height="2"/>
      </g>
      <g fill="#2e8b3a"><rect x="206" y="35" width="14" height="4"/><rect x="206" y="49" width="10" height="4"/><rect x="206" y="70" width="16" height="4"/><rect x="206" y="91" width="8" height="4"/></g>
      <g fill="#d9362b"><rect x="206" y="42" width="6" height="4"/><rect x="206" y="63" width="9" height="4"/><rect x="206" y="84" width="5" height="4"/></g>
    </svg>
    <p class="side-caption" style="top:343px">Constantly track the quality and performance of individual distribution outlets based on the underwriting score of each policy</p>
  </aside>

  <h2 class="tab-dark">Let Brightfen Metrics Build Your Portfolio Analysis Report</h2>
  <footer class="closing">
    <p class="closing-text">The report details your portfolio trends and identifies future unseen problems before they occur. The insight provided in the report exhibits what is actually going on in your portfolio. This likely includes adverse selection, impact of price changes with unintended consequences, and the emerging trends in the composition of the book. The analysis results not only reveal past trends, but also predict future impact.</p>
  </footer>
</main>
</body>
</html>
```